I need a business card design for a new company that will be doing consulting work around issues of cultural competency, and diversity and inclusion. I would like the design to be crisp and clear with bold but conservative colors and incorporate shades of blue

Target Market(s)

Small businesses, schools, non-profits

Industry/Entity Type

Consulting

Font styles to use
Serif
Sans Serif

Colors
0c5ba6
6b449b
3276b5
0292cd

Requirements
Must have
• A Morrow Venture (name of company)
• Lemlem Tavish
• CEO
• lemlem@amorrowventure.com
• (215)483-2756

```html
<!DOCTYPE html>
<html lang="en">
<head>
<meta charset="utf-8">
<title>A Morrow Venture — Business Card</title>
<link rel="stylesheet" href="https://fonts.googleapis.com/css2?family=Montserrat:wght@400&family=Source+Serif+4:opsz,wght@8..60,400;8..60,700&display=swap">
<style>
  :root {
    --card-blue: #1792ce;
    --ink-dark: #16161f;
    --ink-light: #ffffff;
    --sans: "Montserrat", Arial, sans-serif;
    --serif: "Source Serif 4", Georgia, serif;
  }
  * { margin: 0; padding: 0; box-sizing: border-box; }
  html, body {
    width: 1200px;
    height: 684px;
    overflow: hidden;
    background: var(--card-blue);
  }
  .card {
    position: relative;
    width: 1200px;
    height: 684px;
    background: var(--card-blue);
  }
  .card > * {
    position: absolute;
    left: 0;
    width: 100%;
    text-align: center;
  }
  .company-name {
    top: 126px;
    font-family: var(--sans);
    font-weight: 400;
    font-size: 50px;
    line-height: 60px;
    color: var(--ink-dark);
    letter-spacing: 0.5px;
  }
  .divider {
    left: 559px;
    width: 82px;
    height: 4px;
    background: var(--ink-light);
  }
  .divider--top { top: 247px; }
  .divider--bottom { top: 552px; }
  .person-name {
    top: 268px;
    font-family: var(--serif);
    font-weight: 700;
    font-size: 48px;
    line-height: 60px;
    color: var(--ink-light);
  }
  .contact-line {
    font-family: var(--serif);
    font-weight: 400;
    font-size: 34px;
    line-height: 44px;
    color: var(--ink-light);
  }
  .job-title { top: 348px; }
  .email { top: 416px; }
  .phone { top: 487px; }
</style>
</head>
<body>
  <main class="card">
    <h1 class="company-name">A Morrow Venture</h1>
    <div class="divider divider--top"></div>
    <h2 class="person-name">Lemlem Tavish</h2>
    <p class="contact-line job-title">CEO</p>
    <p class="contact-line email">lemlem@amorrowventure.com</p>
    <p class="contact-line phone">(215)483-2756</p>
    <div class="divider divider--bottom"></div>
  </main>
</body>
</html>
```